Chiropractic healthcare group business card

We are a Portland Oregon based chiropractic healthcare group. Looking for a new business card design. Something cutting edge, that shows off our new logo and tag line.Use either of the attached logos.Our tag line = "Who would you be without pain?"I'm open to about anything, impress me!!
Target Market(s)
Chiropractic patients - Auto injury, back pain, sports injuries, neck , shoulder, hip, knee, ankle pain.
Industry/Entity Type
Chiropractic
Contact Information for Business Card
Dr. Bram Holtvick, D.C.
Clinic name - Fernway Chiropractic
2 clinics
location #1
20418 NW Marwick Road
Suite B
North Plains, OR 97133
Location #2
13529 SE Calloway Street
Portland OR 97236
Main phone line 971.555.0143
website : www.FernwayClinics.example
Tag line "Who would you be without pain?"
Colors
Designer to choose colors to be used in the design.
Requirements
Must have
- Use the logo colors -- Want the orange color to be a TRUE orange.
- Both clinic address
- phone number
- website
- personal email - b.holtvick@ReliefBeginsHere.example
- tag line - "Who would you be without pain?"

```html
<!DOCTYPE html>
<html lang="en">
<head>
<meta charset="utf-8">
<title>Fernway Chiropractic – Business Card</title>
<link rel="stylesheet" href="https://fonts.googleapis.com/css2?family=Montserrat:wght@400;500;700&display=swap">
<style>
  :root {
    --orange: #f7931e;
    --charcoal: #56585b;
    --slate: #5f6164;
    --ink: #4a4b4d;
    --paper: #ffffff;
    --backdrop: #e9e8e6;
  }
  * { box-sizing: border-box; margin: 0; padding: 0; }
  html, body { width: 1200px; height: 900px; overflow: hidden; }
  body {
    background: var(--backdrop);
    font-family: "Montserrat", Arial, sans-serif;
    position: relative;
  }
  .card {
    position: absolute;
    top: 296px;
    width: 540px;
    height: 309px;
    overflow: hidden;
    box-shadow: 0 6px 18px rgba(0,0,0,0.18);
  }
  /* back side */
  .card-back { left: 40px; background: var(--slate); }
  .back-brand {
    position: absolute;
    left: 50px;
    top: 60px;
    display: flex;
    align-items: center;
    gap: 14px;
  }
  .brand-square { width: 22px; height: 22px; background: var(--orange); flex: none; }
  .back-brand .brand-name {
    color: var(--paper);
    font-weight: 700;
    font-size: 28px;
    letter-spacing: 4px;
    line-height: 1.15;
    text-transform: uppercase;
  }
  /* front side */
  .card-front { left: 620px; background: var(--paper); color: var(--ink); }
  .doctor-name {
    position: absolute; left: 28px; top: 26px;
    color: var(--orange); font-weight: 700; font-size: 19px;
  }
  .clinic-line {
    position: absolute; left: 28px; top: 52px;
    font-size: 13.5px; font-weight: 500;
  }
  .contact-list {
    position: absolute; left: 28px; top: 96px;
    list-style: none; font-size: 13px; font-weight: 500; line-height: 20px;
  }
  .contact-list li { display: flex; align-items: center; gap: 8px; }
  .contact-list svg { width: 13px; height: 13px; flex: none; }
  .divider {
    position: absolute; left: 28px; right: 26px; top: 150px;
    height: 1.5px; background: var(--charcoal);
  }
  .address { position: absolute; font-size: 13.5px; font-weight: 500; line-height: 19px; }
  .address-north { left: 28px; top: 164px; }
  .address-south { right: 26px; top: 164px; text-align: left; }
  .front-brand {
    position: absolute; right: 26px; top: 70px;
    display: flex; align-items: center; gap: 10px;
  }
  .front-brand .brand-square { width: 16px; height: 16px; }
  .front-brand .brand-name {
    color: var(--charcoal); font-weight: 700; font-size: 19px;
    letter-spacing: 3px; line-height: 1.15; text-transform: uppercase;
  }
  .tagline {
    position: absolute; left: 28px; top: 234px;
    font-size: 14px; font-weight: 500;
  }
  .footer-band {
    position: absolute; left: 0; right: 0; bottom: 0; height: 40px;
  }
  .footer-band svg { position: absolute; inset: 0; }
  .website {
    position: absolute; right: 26px; bottom: 10px;
    color: var(--paper); font-size: 14px; font-weight: 500;
  }
</style>
</head>
<body>
  <section class="card card-back" aria-label="Card back">
    <div class="back-brand">
      <span class="brand-square"></span>
      <span class="brand-name">Fernway<br>Chiropractic</span>
    </div>
  </section>

  <section class="card card-front" aria-label="Card front">
    <h1 class="doctor-name">Dr. Bram Holtvick, D.C.</h1>
    <p class="clinic-line">Clinic name - Fernway Chiropractic</p>

    <ul class="contact-list">
      <li>
        <svg viewBox="0 0 24 24" aria-hidden="true"><path fill="#f7931e" d="M6.6 10.8a15.1 15.1 0 0 0 6.6 6.6l2.2-2.2a1 1 0 0 1 1-.25 11.4 11.4 0 0 0 3.6.6 1 1 0 0 1 1 1V20a1 1 0 0 1-1 1A17 17 0 0 1 3 4a1 1 0 0 1 1-1h3.5a1 1 0 0 1 1 1c0 1.25.2 2.45.6 3.6a1 1 0 0 1-.25 1z"/></svg>
        971.555.0143
      </li>
      <li>
        <svg viewBox="0 0 24 24" aria-hidden="true"><path fill="#f7931e" d="M2 5h20v14H2z"/><path d="M2 5l10 8 10-8" fill="none" stroke="#fff" stroke-width="2"/></svg>
        b.holtvick@ReliefBeginsHere.example
      </li>
    </ul>

    <div class="front-brand">
      <span class="brand-square"></span>
      <span class="brand-name">Fernway<br>Chiropractic</span>
    </div>

    <div class="divider"></div>

    <p class="address address-north">20418 NW Marwick Road, Suite B<br>North Plains, OR 97133</p>
    <p class="address address-south">13529 SE Calloway Street<br>Portland OR 97236</p>

    <p class="tagline">Who would you be without pain?</p>

    <div class="footer-band">
      <svg viewBox="0 0 540 40" preserveAspectRatio="none" aria-hidden="true">
        <polygon points="0,28 300,28 292,40 0,40" fill="#5f6164"/>
        <polygon points="300,4 540,4 540,40 276,40" fill="#f7931e"/>
      </svg>
      <span class="website">www.FernwayClinics.example</span>
    </div>
  </section>
</body>
</html>
```